Info graphic to explain a fee hierarchy

We need a clean and current feeling graphical representation of what a typical fee structure looks like from our competitors, with an accompanying one highlighting the simplicity and transparency of ours.

We will be using this online on our web page and in blog posts. Solutions that can be animated would be looked upon favourably.
however, ideally would like to avoid any Flash based solutions.

I have provided the fee structure comparison and some notes for each component of a typical fee in both excel and a jpg of the excel file. Not fussed with the graph design however a 'stacked' fee graph could get the point across nicely. Up to you.

I have provided a low and high estimate for our competitors. You don't have to include the figures however the proportions in the graph could be a way around cluttering the design with numbers.

I have also included our logo to give you an idea of colours.

Target Market(s)

Gen X and Gen y, internet savvy, financially competent

Industry/Entity Type

Financial Service

Font styles to use
Sans Serif

Requirements
Must have
• Graphical based solution - easy to read and understand
Nice to have
• Potential to be animated, PSD (or similar) with layering so that it is easy to implement for use with HTML 5 or JQuery web pages
Should not have
• Flash solutions

```html
<!DOCTYPE html>
<html lang="en">
<head>
<meta charset="utf-8">
<title>Clients Total Fee Structure</title>
<link href="https://fonts.googleapis.com/css2?family=Oswald:wght@500;700&display=swap" rel="stylesheet">
<style>
:root{
  --ink:#000;
  --note:#6b6b6b;
  --bg:#fff;
  --orange:#fd8a2c;
  --blue:#4d8bcb;
  --legend-orange:#e59a5c;
  --legend-blue:#8f9aa8;
  --brand:#1e2f6e;
}
*{margin:0;padding:0;box-sizing:border-box}
html,body{width:979px;height:1200px;overflow:hidden;background:var(--bg)}
body{position:relative;font-family:'Oswald',sans-serif;color:var(--ink)}
.abs{position:absolute}
.title{font-weight:700;font-size:32px;left:0;width:979px;text-align:center;line-height:1;letter-spacing:-.2px}
.label{font-weight:700;font-size:29px;text-align:right;line-height:1;white-space:nowrap;letter-spacing:-.2px}
.note{font-weight:500;font-size:22px;color:var(--note);line-height:1;white-space:nowrap;letter-spacing:-.1px}
.bar{height:25px}
.legend{font-weight:700;font-size:31px;line-height:1;white-space:nowrap;letter-spacing:-.4px}
.legend .low{color:var(--legend-orange)}
.legend .high{color:var(--legend-blue)}
.tag{font-weight:700;font-size:27px;line-height:1;white-space:nowrap;color:var(--legend-orange);letter-spacing:-.3px}
.figure{font-weight:700;font-size:21px;line-height:1;white-space:nowrap}
.brand{left:112px;top:1012px;display:flex;align-items:center;gap:12px;font-weight:700;font-size:40px;color:var(--brand);line-height:1}
.brand .dot{width:16px;height:16px;border-radius:50%;background:var(--brand)}
</style>
</head>
<body>

<section class="retail">
  <h1 class="abs title" style="top:53px">Clients Total Fee Structure - Typical Retail Super Fund</h1>
  <div class="abs legend" style="left:453px;top:101px"><span class="low">Low end ranging to </span><span class="high">high end</span></div>

  <div class="abs label" style="right:598px;top:128px">Adviser Fee</div>
  <div class="abs bar" style="left:394px;top:133px;width:285px;background:#fd8a2c"></div>
  <div class="abs bar" style="left:679px;top:133px;width:134px;background:#4d8bcb"></div>
  <div class="abs note" style="left:395px;top:160px">Adviser cost for ongoing service arrangement</div>

  <div class="abs label" style="right:598px;top:185px">Dealer Group</div>
  <div class="abs bar" style="left:394px;top:191px;width:176px;background:#fd9137"></div>
  <div class="abs bar" style="left:570px;top:191px;width:85px;background:#5592d0"></div>
  <div class="abs note" style="left:395px;top:217px">Cost of Aust. Fin. Service&nbsp; Licensing and product selection</div>

  <div class="abs label" style="right:598px;top:240px">Platform Fee</div>
  <div class="abs bar" style="left:394px;top:245px;width:222px;background:#fd9137"></div>
  <div class="abs bar" style="left:616px;top:245px;width:193px;background:#6a9fd3"></div>
  <div class="abs note" style="left:395px;top:272px">Cost of providing the investment platform</div>

  <div class="abs label" style="right:598px;top:297px">Trustee Fee</div>
  <div class="abs bar" style="left:394px;top:303px;width:176px;background:#fda055"></div>
  <div class="abs bar" style="left:570px;top:303px;width:66px;background:#78a3d1"></div>
  <div class="abs note" style="left:395px;top:329px">Superannuation Trustee Fee</div>

  <div class="abs label" style="right:598px;top:353px">Asset Allocation fee</div>
  <div class="abs bar" style="left:394px;top:358px;width:70px;background:#fca962"></div>
  <div class="abs bar" style="left:464px;top:358px;width:107px;background:#7ea7d2"></div>
  <div class="abs note" style="left:393px;top:384px">Cost of choosing between Equities, bonds, cash</div>

  <div class="abs label" style="right:598px;top:409px">Investment Board Fee</div>
  <div class="abs bar" style="left:394px;top:414px;width:202px;background:#fdb070"></div>
  <div class="abs bar" style="left:596px;top:414px;width:34px;background:#87a9cf"></div>
  <div class="abs note" style="left:395px;top:441px">Cost of selecting various equities or bonds manager</div>

  <div class="abs label" style="right:598px;top:465px">Investment Management Fee</div>
  <div class="abs bar" style="left:394px;top:469px;width:285px;background:#febd8a"></div>
  <div class="abs bar" style="left:679px;top:469px;width:103px;background:#92b0cf"></div>
  <div class="abs note" style="left:397px;top:496px">Actual Fee going to the investment managers</div>

  <div class="abs label" style="right:598px;top:520px">Total</div>
  <div class="abs bar" style="left:394px;top:526px;width:442px;background:#fed0a8"></div>
  <div class="abs bar" style="left:836px;top:526px;width:108px;background:#adbccd"></div>
  <div class="abs figure" style="left:750px;top:557px">1.35%</div>
  <div class="abs figure" style="left:834px;top:557px">to</div>
  <div class="abs figure" style="left:884px;top:557px">3.55%</div>
</section>

<section class="house">
  <h2 class="abs title" style="top:656px">Clients Total Fee Structure - Quarnell</h2>

  <div class="abs tag" style="right:197px;top:708px">Low end</div>
  <div class="abs label" style="right:492px;top:731px">Platform Fee (including Trustee Fee)</div>
  <div class="abs bar" style="left:497px;top:735px;width:285px;background:var(--orange)"></div>
  <div class="abs tag" style="right:197px;top:759px">High end</div>
  <div class="abs bar" style="left:497px;top:786px;width:285px;background:var(--blue)"></div>
  <div class="abs note" style="left:496px;top:813px">Cost of providing the investment platform</div>

  <div class="abs label" style="right:492px;top:841px">Investment Management Fee</div>
  <div class="abs bar" style="left:497px;top:845px;width:176px;background:var(--orange)"></div>
  <div class="abs bar" style="left:497px;top:897px;width:176px;background:var(--blue)"></div>
  <div class="abs note" style="left:496px;top:926px">Actual Fee going to the investment managers</div>

  <div class="abs label" style="right:492px;top:953px">Total</div>
  <div class="abs bar" style="left:497px;top:960px;width:414px;background:var(--orange)"></div>
  <div class="abs bar" style="left:497px;top:1009px;width:416px;background:var(--blue)"></div>
  <div class="abs figure" style="right:65px;top:1041px">1.00%</div>

  <div class="abs brand"><span class="dot"></span><span>Quarnell Wealth</span></div>
</section>

</body>
</html>
```